Weight Loss Challenge Social Media Graphics

Create 6-7 individual social media graphics (square size) to encourage folks to join our weight loss challenge. For the color scheme of the graphics, use the color palette attached

Note: each graphic can contain any of the stock photography attached or just the single picture of me (brown shirt) but a few should be ONLY the text
For some graphics we can say: JOIN US!
For some graphics, use only TEXT based

primarily women who want to get healthy

health and weight loss

• The largest text should be: Bright Body Reset

```html
<!DOCTYPE html>
<html lang="en">
<head>
<meta charset="UTF-8">
<title>Bright Body Reset – Join Us</title>
<link rel="stylesheet" href="https://fonts.googleapis.com/css2?family=Italiana&family=Arimo:wght@400&family=Cormorant+Garamond:wght@500&display=swap">
<style>
  :root {
    --rose-clay: #c29d93;
    --cream: #f4e2d8;
    --blush: #ffe1ec;
  }
  * { margin: 0; padding: 0; box-sizing: border-box; }
  html, body {
    width: 1200px;
    height: 1200px;
    overflow: hidden;
    background: var(--rose-clay);
  }
  .promo {
    position: relative;
    width: 1200px;
    height: 1200px;
    background: var(--rose-clay);
    color: var(--cream);
  }
  .promo__title {
    position: absolute;
    top: 232px;
    left: 0;
    width: 1200px;
    text-align: center;
    font-family: "Italiana", serif;
    font-weight: 400;
    font-size: 136px;
    line-height: 1;
    white-space: nowrap;
    letter-spacing: 1px;
  }
  .promo__offer {
    position: absolute;
    top: 446px;
    left: 0;
    width: 1188px;
    text-align: center;
    font-family: "Arimo", sans-serif;
    font-size: 37px;
    line-height: 66px;
    letter-spacing: 0.5px;
    text-transform: uppercase;
  }
  .promo__cta {
    position: absolute;
    top: 652px;
    left: 292px;
    width: 616px;
    height: 154px;
    background: var(--blush);
    color: var(--rose-clay);
    display: flex;
    align-items: center;
    justify-content: center;
    font-family: "Arimo", sans-serif;
    font-size: 92px;
    letter-spacing: 3px;
    text-transform: uppercase;
  }
  .promo__date {
    position: absolute;
    top: 954px;
    left: 0;
    width: 1260px;
    text-align: center;
    font-family: "Cormorant Garamond", serif;
    font-weight: 500;
    font-size: 44px;
    letter-spacing: 2.5px;
    text-transform: uppercase;
  }
</style>
</head>
<body>
  <main class="promo">
    <h1 class="promo__title">Bright Body Reset</h1>
    <p class="promo__offer">Lose up to 20 pounds<br>in 6 weeks!</p>
    <div class="promo__cta">Join us!</div>
    <p class="promo__date">Begins Monday, Jan 6th</p>
  </main>
</body>
</html>
```